Vertical flyer design to guide people to my shop

We need a vertical flyer design for a tailor shop, Marlow Stitchworks. Our shop is on the 3/F, and we need this flyer/poster to placed on the G/F street level to guide people to take the lifts upstairs. Basically to tell people that, "We are here on 3/F!"

Dimensions ratio: 80 (wide) x200 (tall)

You may use the photos and graphics from the webpages below.
http://www.marlowstitchworks.net/en/marlow-stitchworks-hong-kong-tailors-tailor-shop/

https://www.cloth-q.com/tailor/marlow-stitchworks

```html
<!DOCTYPE html>
<html lang="en">
<head>
<meta charset="utf-8">
<title>Marlow Stitchworks – We are here on 3/F</title>
<link rel="stylesheet" href="https://fonts.googleapis.com/css2?family=Tinos:wght@400;700&family=Yellowtail&display=swap">
<style>
  :root {
    --paper: #ffffff;
    --ink: #111111;
    --accent-red: #d0202a;
    --chevron-light: #8a8a8a;
    --chevron-dark: #3c3c3c;
    --chevron-mark: #b9b9b9;
    --ornament-tone: #e6e6e6;
    --cloth-red: #7a1119;
    --cloth-deep: #3a070b;
    --night: #000000;
    --lift-text: #ffffff;
  }
  * { margin: 0; padding: 0; box-sizing: border-box; }
  html, body { width: 1200px; height: 2764px; overflow: hidden; background: var(--paper); }
  .flyer {
    position: relative;
    width: 1200px;
    height: 2764px;
    background: var(--paper);
    overflow: hidden;
    color: var(--ink);
  }
  .border-ornament {
    position: absolute;
    top: 115px;
    width: 160px;
    height: 1600px;
    background: linear-gradient(180deg, var(--ornament-tone), #f4f4f4 50%, var(--ornament-tone));
    border-radius: 80px 80px 40px 40px;
  }
  .border-ornament--left { left: 80px; }
  .border-ornament--right { right: 80px; }

  .shop-name {
    position: absolute;
    top: 240px;
    left: 0;
    width: 100%;
    text-align: center;
    font-family: "Tinos", "Times New Roman", serif;
    font-weight: 700;
    line-height: 1;
    text-transform: uppercase;
  }
  .shop-name__first { display: block; font-size: 100px; letter-spacing: 2px; }
  .shop-name__second { display: block; font-size: 72px; margin-top: 14px; }

  .shop-tagline {
    position: absolute;
    top: 500px;
    left: 0;
    width: 100%;
    text-align: center;
    font-family: "Tinos", "Times New Roman", serif;
    font-size: 46px;
    line-height: 80px;
    text-transform: uppercase;
  }

  .direction-chevrons {
    position: absolute;
    top: 770px;
    left: 400px;
    width: 400px;
    height: 360px;
  }

  .location-callout {
    position: absolute;
    top: 1180px;
    left: 0;
    width: 100%;
    text-align: center;
  }
  .location-callout__lead,
  .location-callout__floor {
    display: block;
    font-family: "Yellowtail", cursive;
    font-size: 150px;
    line-height: 1;
  }
  .location-callout__here {
    display: block;
    font-family: "Tinos", "Times New Roman", serif;
    font-weight: 700;
    font-size: 190px;
    line-height: 1;
    color: var(--accent-red);
    letter-spacing: 4px;
    margin: 10px 0 0;
  }
  .location-callout__floor { margin-top: 0; }

  .workshop-photo {
    position: absolute;
    left: 0;
    top: 0;
    width: 1200px;
    height: 2764px;
  }

  .lift-note {
    position: absolute;
    left: 0;
    top: 2590px;
    width: 100%;
    text-align: center;
    font-family: Arial, Helvetica, sans-serif;
    font-size: 30px;
    color: var(--lift-text);
  }
</style>
</head>
<body>
<main class="flyer">
  <div class="border-ornament border-ornament--left" role="img" aria-label="Black scrolling vine ornament running down the left edge"></div>
  <div class="border-ornament border-ornament--right" role="img" aria-label="Black scrolling vine ornament running down the right edge"></div>

  <h1 class="shop-name">
    <span class="shop-name__first">Marlow</span>
    <span class="shop-name__second">Stitchworks</span>
  </h1>

  <p class="shop-tagline">Expert Ladies’<br>&amp; Gent’s Tailors</p>

  <svg class="direction-chevrons" viewBox="0 0 400 360" aria-label="Upward chevrons numbered 1 to 3">
    <defs>
      <linearGradient id="chevron-fill" x1="0" y1="0" x2="0" y2="1">
        <stop offset="0" stop-color="var(--chevron-light)"/>
        <stop offset="1" stop-color="var(--chevron-dark)"/>
      </linearGradient>
    </defs>
    <polygon points="200,0 400,130 200,70 0,130" fill="url(#chevron-fill)"/>
    <polygon points="200,115 370,235 200,180 30,235" fill="url(#chevron-fill)"/>
    <polygon points="200,225 340,340 200,290 60,340" fill="url(#chevron-fill)"/>
    <g fill="var(--chevron-mark)" font-family="Tinos, serif" font-size="22" text-anchor="middle">
      <text x="200" y="48">3</text>
      <text x="200" y="160">2</text>
      <text x="200" y="270">1</text>
    </g>
  </svg>

  <h2 class="location-callout">
    <span class="location-callout__lead">We are</span>
    <span class="location-callout__here">HERE</span>
    <span class="location-callout__floor">on 3/F</span>
  </h2>

  <svg class="workshop-photo" viewBox="0 0 1200 2764" aria-hidden="false">
    <defs>
      <linearGradient id="cloth-tone" x1="0" y1="0" x2="0" y2="1">
        <stop offset="0" stop-color="var(--cloth-deep)"/>
        <stop offset="0.25" stop-color="var(--cloth-red)"/>
        <stop offset="0.72" stop-color="var(--cloth-red)"/>
        <stop offset="0.88" stop-color="var(--night)"/>
        <stop offset="1" stop-color="var(--night)"/>
      </linearGradient>
    </defs>
    <polygon points="0,1850 620,1745 1200,1850 1200,2764 0,2764" fill="url(#cloth-tone)" role="img" aria-label="Photo of a roll of red tailoring cloth with threads, tape measure and a tailor's hands at work"/>
    <polyline points="0,1850 620,1745 1200,1850" fill="none" stroke="var(--ink)" stroke-width="6"/>
  </svg>

  <p class="lift-note">take the lifts upstairs</p>
</main>
</body>
</html>
```